Corvalith business website

I am wanting a website for my media agency Corvalith.

It needs to be be an attractive, unique and professional looking website. The website is a destination for people to be able to understand the service that Corvalith offers.

Please read uploaded website copy to gain an understanding of the business.

Target Market(s)

small business owners, business decision makers, marketing managers,

Industry/Entity Type

Business

Requirements
Must have
• Good branding.

```html
<!DOCTYPE html>
<html lang="en">
<head>
<meta charset="utf-8">
<title>Corvalith Media</title>
<link rel="stylesheet" href="https://fonts.googleapis.com/css2?family=Lora:ital,wght@1,400;1,700&family=PT+Sans:ital,wght@0,400;0,700;1,400&family=PT+Sans+Narrow&display=swap">
<style>
:root{
  --blue:#0000c8;
  --navy:#00005e;
  --ink:#444;
  --grey-bg:#f2f2f2;
  --footer:#2e2e2e;
  --white:#fff;
}
*{margin:0;padding:0;box-sizing:border-box}
html,body{width:1083px;height:1200px;overflow:hidden}
body{position:relative;font-family:"PT Sans",Arial,sans-serif;color:var(--ink);background:var(--grey-bg)}
.abs{position:absolute}
.topline{left:0;top:0;width:1083px;height:7px;background:#8a8a8a}
.header{left:0;top:7px;width:1083px;height:83px;background:linear-gradient(100deg,#e9e9e9 0%,#f7f7f7 50%,#e6e6e6 100%)}
.brand{left:124px;top:30px;display:flex;align-items:center;gap:8px;font-weight:700;font-size:22px;color:var(--blue)}
.brand-mark{width:22px;height:22px;background:var(--blue)}
.contact{left:771px;font-family:"PT Sans Narrow",sans-serif;font-size:16px;color:#555;display:flex;align-items:center;gap:8px}
.social{top:68px;display:flex;gap:6px;left:866px}
.social span{width:19px;height:19px;border-radius:2px;display:block}
.band{left:0;top:90px;width:1083px;height:343px;background:linear-gradient(90deg,#00009a 0%,#0000e0 50%,#00009a 100%);border-bottom:3px solid var(--navy)}
.nav{left:124px;top:90px;width:835px;height:46px;border-left:1px solid #2a2ab0;border-right:1px solid #2a2ab0;background:linear-gradient(#00006e,#00008c)}
.nav a{color:var(--white);text-decoration:none;font-size:11px;font-weight:700;line-height:46px;position:absolute;top:0}
.slide-frame{left:124px;top:136px;width:835px;height:262px;background:var(--white);box-shadow:0 8px 22px rgba(0,0,40,.55)}
.slide-img{left:132px;top:144px;width:819px;height:246px;background:linear-gradient(90deg,#f2f4f9 0%,#e4e8f2 45%,#cfd6e6 75%,#e2e6ef 100%)}
.slide-text{left:158px;top:152px;width:470px;font-family:"Lora",Georgia,serif;font-style:italic;font-size:30px;line-height:35px;color:#555}
.cta{left:158px;top:325px;width:195px;height:53px;background:linear-gradient(#4a4a4a,#1f1f1f);border-radius:5px;border:1px solid #777;color:var(--white)}
.cta .div{position:absolute;left:48px;top:3px;width:1px;height:47px;background:#666}
.cta .t{position:absolute;left:59px;top:10px;font-size:15px;font-weight:700}
.cta small{position:absolute;left:59px;top:31px;font-size:10px}
.dots{left:498px;top:408px;display:flex;gap:6px}
.dots span{width:13px;height:13px;border-radius:50%;background:#5a5ae6}
.dots span.on{background:var(--white)}
.notch{left:530px;top:433px}
.welcome{left:0;top:436px;width:1083px;height:112px;background:var(--grey-bg)}
.welcome h1{position:absolute;top:22px;width:100%;text-align:center;font-family:"Lora",serif;font-style:italic;font-weight:700;font-size:18px;color:var(--blue)}
.welcome p{position:absolute;top:52px;width:100%;text-align:center;font-family:"Lora",serif;font-style:italic;font-size:15px;line-height:25px;color:#555}
.welcome a{position:absolute;left:884px;top:82px;font-size:11px;font-weight:700;color:var(--blue);text-decoration:none}
.services{left:0;top:548px;width:1083px;height:331px;background:linear-gradient(#fff,#f4f4f4)}
.card{top:582px;width:262px;height:239px;background:var(--white);border:1px solid #ddd;border-radius:3px;box-shadow:0 3px 8px rgba(0,0,0,.15)}
.card h2{height:29px;background:linear-gradient(#0000a8,#0000d8);color:var(--white);font-size:14px;font-weight:700;padding:5px 9px}
.card .pic{margin:12px 14px 0;height:98px}
.card p{margin:15px 14px 0;width:228px;font-size:11.2px;line-height:15.2px;color:#555}
.more{top:841px;height:17px;padding:0 22px 0 7px;background:linear-gradient(#777,#444);border-radius:9px;color:var(--white);font-size:10px;font-weight:700;line-height:17px}
.more::after{content:"";position:absolute;right:5px;top:3px;width:11px;height:11px;border-radius:50%;background:var(--white)}
.more i{position:absolute;right:8px;top:6px;border-left:5px solid #444;border-top:3px solid transparent;border-bottom:3px solid transparent;z-index:1}
.lower{left:0;top:879px;width:1083px;height:169px;background:var(--grey-bg)}
.h3{font-size:17px;font-weight:700;color:var(--navy)}
.clients{left:124px;top:927px;width:540px;height:100px;background:#fafafa;border:1px solid #e2e2e2;border-radius:3px}
.client-row{left:30px;top:38px;width:480px;display:flex;justify-content:space-between;font-size:16px;font-weight:700;color:#b5b5b5}
.quote{left:721px;top:933px;width:220px;font-size:11px;line-height:16.5px;font-style:italic;color:#555;text-indent:27px}
.qname{left:713px;top:1007px;width:234px;height:20px;background:#dcdcdc;text-align:right;padding-right:10px;font-size:11px;font-weight:700;line-height:20px;color:#333}
.footer{left:0;top:1048px;width:1083px;height:152px;background:var(--footer)}
.fnav{top:1058px;font-size:11px;font-weight:700;color:var(--white)}
.fline{left:124px;top:1080px;width:835px;height:1px;background:#444}
.fbrand{left:0;top:1104px;width:1083px;display:flex;justify-content:center;align-items:center;gap:7px;font-size:16px;font-weight:700;color:#8a8a8a}
.fbrand span.sq{width:16px;height:16px;background:#6a6a6a}
.faddr{top:1157px;width:1083px;text-align:center;font-size:10.5px;color:#eee}
.fcopy{top:1180px;width:1083px;text-align:center;font-size:9px;color:#ddd}
</style>
</head>
<body>
<div class="abs topline"></div>
<header class="abs header"></header>
<div class="abs brand"><span class="brand-mark"></span>Corvalith</div>
<div class="abs contact" style="top:14px">
  <svg width="16" height="16" viewBox="0 0 16 16"><circle cx="8" cy="8" r="7" fill="none" stroke="#666" stroke-width="1.2"/><path d="M6 4c-1 1-1 4 1 7l1-1-1-2 1-1-1-3z" fill="#666"/></svg>(02) 5550 1372</div>
<div class="abs contact" style="top:41px">
  <svg width="16" height="12" viewBox="0 0 16 12"><rect x=".5" y=".5" width="15" height="11" fill="none" stroke="#666"/><path d="M.5 .5 8 7 15.5 .5" fill="none" stroke="#666"/></svg>info@corvalith.com.au</div>
<div class="abs social"><span style="background:#3b5ba6"></span><span style="background:#33a9e0"></span><span style="background:#c4302b"></span><span style="background:#333"></span></div>

<div class="abs band"></div>
<nav class="abs nav">
  <a style="left:34px">HOME</a><a style="left:123px">ABOUT US</a><a style="left:233px">WHAT WE DO</a><a style="left:354px">PEOPLE</a><a style="left:446px">IDEAS</a><a style="left:530px">CONTACT US</a>
</nav>

<div class="abs slide-frame"></div>
<div class="abs slide-img" role="img" aria-label="Blue chess king standing before a row of white pawns"></div>
<div class="abs slide-text">We are marketing partners in our clients businesses and enjoy seeing them grow and achieve their goals.</div>
<div class="abs cta">
  <svg style="position:absolute;left:13px;top:14px" width="24" height="24" viewBox="0 0 24 24"><path d="M2 8h10V2l10 10-10 10v-6H2z" fill="#7ccf3a"/></svg>
  <span class="div"></span><span class="t">FIND OUT MORE</span><small>How we can <b>help you</b></small>
</div>
<div class="abs dots"><span class="on"></span><span></span><span></span><span></span><span></span></div>

<section class="abs welcome">
  <h1>Welcome to Corvalith Media</h1>
  <p>Corvalith is a media strategy, planning and buying agency. We work with both small and big businesses.<br>Corvalith Works across all offline platforms (radio, press</p>
  <a>Read more</a>
</section>
<svg class="abs notch" width="24" height="16" viewBox="0 0 24 16"><path d="M0 0h24L12 14z" fill="var(--navy)"/></svg>

<section class="abs services"></section>
<article class="abs card" style="left:125px">
  <h2>Media Strategy &amp; Planning</h2>
  <div class="pic" role="img" aria-label="Highlighted strategy text on paper" style="background:linear-gradient(90deg,#f4f4f4 0%,#e8e8e8 50%,#7ad35e 75%,#2c2c2c 100%)"></div>
  <p>Using accurate analysis we provide relevant research about the consumer or business target &amp; trends in the market place. A tailored strategy is devised that comprises of the right media channels that fit with the</p>
</article>
<article class="abs card" style="left:419px">
  <h2>Media Trading &amp; Campaign Monitoring</h2>
  <div class="pic" role="img" aria-label="Charts on screen and hand drawing a growth graph" style="background:linear-gradient(90deg,#cfd9ef 0%,#eef1f7 45%,#f6f6f6 70%,#d9d2c8 100%)"></div>
  <p>Using our media partner relationships, trade negotiation techniques &amp; experience we achieve a high level of value for all media buys that leads to significant cost savings for clients.</p>
</article>
<article class="abs card" style="left:697px">
  <h2>Content &amp; Creative</h2>
  <div class="pic" role="img" aria-label="Hand writing in a notepad beside a keyboard" style="background:linear-gradient(135deg,#1b2536 0%,#44536a 40%,#d8dbe0 70%,#eef0f3 100%)"></div>
  <p>Creating imaginative &amp; interesting content for a brand can be a great way of achieving a high level of engagement to a target audience. Content can be published and broadcast on a variety of different media platforms.</p>
</article>
<div class="abs more" style="left:283px">Read More<i></i></div>
<div class="abs more" style="left:584px">Read More<i></i></div>
<div class="abs more" style="left:868px">Read More<i></i></div>

<section class="abs lower"></section>
<h3 class="abs h3" style="left:124px;top:899px">Our Clients</h3>
<div class="abs clients">
  <svg class="abs" style="left:6px;top:44px" width="8" height="10"><path d="M7 0v10L0 5z" fill="#777"/></svg>
  <div class="abs client-row"><span>Novarex</span><span>Pellwin</span><span>Dorcastle</span><span>Quinara</span><span>Halbridge</span></div>
  <svg class="abs" style="left:526px;top:44px" width="8" height="10"><path d="M0 0v10l7-5z" fill="#777"/></svg>
</div>
<h3 class="abs h3" style="left:715px;top:896px">Testimonials</h3>
<svg class="abs" style="left:714px;top:926px" width="28" height="18" viewBox="0 0 28 18"><path d="M2 18c-2-8 2-16 10-18-4 4-4 8-2 10zM16 18c-2-8 2-16 10-18-4 4-4 8-2 10z" fill="#d6d6d6"/></svg>
<p class="abs quote">Praesent ut diam purus, eu adipiscing dolor. Proin purus orci, rhoncus sit amet ullamcorper in, ornare sit amet lectus. Donec at nulla purus.</p>
<svg class="abs" style="left:793px;top:985px" width="28" height="18" viewBox="0 0 28 18"><path d="M26 0c2 8-2 16-10 18 4-4 4-8 2-10zM12 0c2 8-2 16-10 18 4-4 4-8 2-10z" fill="#d6d6d6"/></svg>
<div class="abs qname">- &nbsp;LOREM NAME</div>

<footer class="abs footer"></footer>
<span class="abs fnav" style="left:262px">HOME</span>
<span class="abs fnav" style="left:352px">ABOUT US</span>
<span class="abs fnav" style="left:461px">WHAT WE DO</span>
<span class="abs fnav" style="left:583px">PEOPLE</span>
<span class="abs fnav" style="left:674px">IDEAS</span>
<span class="abs fnav" style="left:758px">CONTACT US</span>
<div class="abs fline"></div>
<div class="abs fbrand"><span class="sq"></span>Corvalith</div>
<p class="abs faddr">PO Box XXX XXX Sydney Australia &nbsp; | &nbsp; Phone: &nbsp;02.5550 1372 &nbsp; | &nbsp; Email: &nbsp;info@corvalith.com.au</p>
<p class="abs fcopy">Copyright © 2013 &nbsp;CorvalithMedia. | All Rights Reserved</p>
</body>
</html>
```